Allied Health team of Physiotherapists & Occupational Therapists seek a business card design

We have our new logo, we now need our new business cards and stationary. Willowmere: Oedema & Family Clinic is seeking a generic card design to represent our whole team and individual cards for each therapist that incorporates our new logo to communicate our holistic approach that is calming, nuturing, supportive and welcoming.
Our Physiotherapists and Occupational Therapists assess, treat and provide education for people who are at risk of or who have lymphoedema. This is often as a result of treatment for cancer. We provide pre-operative and post-operative management and cancer rehabilitation in our Pilates studio. Our team also consists of Physiotherapists who have a strong interest in pelvic floor and continence management for both men and women.

Target Market(s)

Mainly women health conscious

Industry/Entity Type

Allied Health: Physiotherapy / Occupational Therapy

Contact Information for Business Card

Address: 14 Tannerly Ave Larchmont Bay 3471 Phone: 84317756 fax: 8431 7759 Email: info@willowmerecareco.com.au Website: willowmerecareco.com.au Facebook address: facebook.com/WillowmereOedemaAndFamilyCareCentre. Room to write appointments. Individual cards need to have name, office email and individual email and professional details

Requirements
Must have
• Logo as per uploaded documents

```html
<!DOCTYPE html>
<html lang="en">
<head>
<meta charset="utf-8">
<title>Willowmere Business Cards</title>
<link href="https://fonts.googleapis.com/css2?family=Philosopher:ital,wght@0,400;0,700;1,400&family=Allura&display=swap" rel="stylesheet">
<style>
  :root {
    --peach: #f9b183;
    --peach-text: #f5a36f;
    --sage: #c5d0c6;
    --ink: #555555;
    --paper: #ffffff;
    --backdrop: #9b9b9b;
  }
  * { box-sizing: border-box; margin: 0; padding: 0; }
  html, body { width: 1133px; height: 1200px; overflow: hidden; }
  body {
    background: var(--backdrop);
    font-family: "Philosopher", sans-serif;
    color: var(--ink);
    position: relative;
  }
  .card {
    position: absolute;
    left: 219px;
    width: 693px;
    height: 397px;
    background: var(--paper);
    overflow: hidden;
  }
  .card--front { top: 152px; }
  .card--back { top: 647px; }

  /* Front */
  .brand-panel {
    position: absolute; left: 0; top: 0;
    width: 247px; height: 100%;
    background: var(--peach);
    border-right: 4px solid var(--sage);
  }
  .brand-mark {
    position: absolute;
    display: flex; align-items: center; justify-content: center;
    text-align: center;
    border-radius: 50%;
    font-family: "Philosopher", sans-serif;
    font-weight: 400;
    font-size: 19px;
    line-height: 1.35;
  }
  .brand-panel .brand-mark {
    left: 18px; top: 93px; width: 205px; height: 205px;
    border: 2px solid var(--paper);
    color: var(--paper);
  }
  .appointment {
    position: absolute; left: 278px; top: 0; right: 0;
  }
  .appointment__title {
    position: absolute; top: 62px; left: 0; width: 370px;
    text-align: center;
    color: var(--peach-text);
    font-weight: 700;
    font-size: 28px;
  }
  .field {
    position: absolute; left: 0; width: 377px;
    display: flex; align-items: flex-end;
    font-size: 15.5px;
  }
  .field__line { flex: 1; border-bottom: 1px solid #777; margin-left: 5px; height: 14px; }
  .field--name { top: 149px; }
  .field--date { top: 193px; }
  .field--time { top: 233px; }
  .contact-row {
    position: absolute; left: 278px;
    display: flex; align-items: center; gap: 8px;
    font-size: 16px;
  }
  .contact-row--address { top: 307px; }
  .contact-row--social { top: 342px; }
  .front-divider {
    position: absolute; left: 278px; right: 0; top: 336px;
    height: 2px; background: var(--sage);
  }
  .icon { width: 15px; height: 15px; flex: none; }

  /* Back */
  .therapist { position: absolute; left: 21px; top: 160px; }
  .therapist__name {
    font-family: "Allura", cursive;
    font-size: 54px;
    color: var(--peach-text);
    line-height: 1;
  }
  .therapist__creds {
    margin-left: 14px; margin-top: 2px;
    font-style: italic; font-size: 13px; line-height: 1.15;
  }
  .therapist__role { margin-left: 14px; font-size: 15.5px; margin-top: 1px; }
  .contact-list {
    position: absolute; left: 35px; top: 280px;
    list-style: none; font-size: 16px; line-height: 17.3px;
  }
  .contact-list li { display: flex; align-items: center; gap: 7px; }
  .card--back .brand-mark {
    left: 431px; top: 30px; width: 220px; height: 220px;
    border: 2px solid var(--peach-text);
    color: var(--peach-text);
    font-size: 21px;
  }
</style>
</head>
<body>

<section class="card card--front" aria-label="Appointment card">
  <div class="brand-panel">
    <div class="brand-mark">Willowmere<br>Oedema &amp;<br>Family Clinic</div>
  </div>

  <div class="appointment">
    <h1 class="appointment__title">Next Appointment</h1>
    <div class="field field--name"><span>Name:</span><span class="field__line"></span></div>
    <div class="field field--date"><span>Date:</span><span class="field__line"></span></div>
    <div class="field field--time"><span>Time:</span><span class="field__line"></span></div>
  </div>

  <div class="contact-row contact-row--address">
    <svg class="icon" viewBox="0 0 16 16"><circle cx="8" cy="8" r="8" fill="var(--peach)"/><path d="M3.5 8.2 8 4.3l4.5 3.9h-1.4V12H9.2V9.5H6.8V12H4.9V8.2z" fill="#666"/></svg>
    <span>14 Tannerly Ave, Larchmont Bay 3471</span>
  </div>
  <div class="front-divider"></div>
  <div class="contact-row contact-row--social">
    <svg class="icon" viewBox="0 0 16 16"><circle cx="8" cy="8" r="8" fill="var(--peach)"/></svg>
    <span>/WillowmereOedemaAndFamilyCareCentre</span>
  </div>
</section>

<section class="card card--back" aria-label="Therapist card">
  <div class="therapist">
    <p class="therapist__name">Marissa Holt</p>
    <p class="therapist__creds">B. Physio<br>Post Grad Certif. Continence &amp; Pelvic Floor Rehabilitation</p>
    <p class="therapist__role">Physiotherapist Pelvic Health</p>
  </div>

  <ul class="contact-list">
    <li><svg class="icon" viewBox="0 0 16 16"><circle cx="8" cy="8" r="8" fill="var(--peach)"/><path d="M4 6.5c0-1 1.8-1.6 4-1.6s4 .6 4 1.6v.8H10.3V6.4H5.7v.9H4zM5 8h6l.8 3.3H4.2z" fill="#666"/></svg>84317756 Phone</li>
    <li><svg class="icon" viewBox="0 0 16 16"><circle cx="8" cy="8" r="8" fill="var(--peach)"/><path d="M5.5 4h5v2.5h-5zM4 7h8v3.5h-1.5V12h-5v-1.5H4z" fill="#666"/></svg>8431 7759 Fax</li>
    <li><svg class="icon" viewBox="0 0 16 16"><circle cx="8" cy="8" r="8" fill="var(--peach)"/><rect x="4" y="5.3" width="8" height="5.4" fill="#666"/><path d="M4 5.3 8 8.4l4-3.1" stroke="var(--peach)" fill="none" stroke-width=".9"/></svg>marissa@willowmerecareco.com.au</li>
    <li><svg class="icon" viewBox="0 0 16 16"><circle cx="8" cy="8" r="8" fill="var(--peach)"/><rect x="4" y="5.3" width="8" height="5.4" fill="#666"/><path d="M4 5.3 8 8.4l4-3.1" stroke="var(--peach)" fill="none" stroke-width=".9"/></svg>info@willowmerecareco.com.au (office)</li>
    <li><svg class="icon" viewBox="0 0 16 16"><circle cx="8" cy="8" r="8" fill="var(--peach)"/><circle cx="8" cy="8" r="3.8" fill="none" stroke="#666" stroke-width="1.2"/><path d="M4.2 8h7.6M8 4.2v7.6" stroke="#666" stroke-width=".9"/></svg>willowmerecareco.com.au</li>
  </ul>

  <div class="brand-mark">Willowmere<br>Oedema &amp;<br>Family Clinic</div>
</section>

</body>
</html>
```